TK Stationary Design

Logo, Business Card, Letterhead & Email Signature Design

Target Market(s)

Legal

Colors

Designer to choose colors to be used in the design.

Requirements
Must have
• Gold and Blue are the colours to use. The TK must be inside the Gold Legal Pendulum

```html
<!DOCTYPE html>
<html lang="en">
<head>
<meta charset="utf-8">
<title>TK Morenkwe Stationery</title>
<link href="https://fonts.googleapis.com/css2?family=Lato:wght@300;400&family=Playfair+Display:wght@700&display=swap" rel="stylesheet">
<style>
:root{
  --frame:#231f20;
  --board:#d1d2d4;
  --paper:#ffffff;
  --blue:#0d6a8c;
  --gold:#b09a6a;
  --gold-light:#dfc27c;
  --ink:#4a4a4a;
  --muted:#6d6e70;
}
*{margin:0;padding:0;box-sizing:border-box}
html,body{width:1200px;height:1200px;overflow:hidden;background:var(--frame);font-family:'Lato',sans-serif}
.canvas{position:relative;width:1200px;height:1200px}
.panel{position:absolute}
.panel--light{left:22px;top:22px;width:585px;height:260px;background:var(--paper)}
.panel--dark{left:607px;top:22px;width:571px;height:260px;background:var(--frame)}
.panel--board{left:22px;top:282px;width:1156px;height:896px;background:var(--board)}
.brand{position:absolute;display:flex;align-items:center;gap:.35em;font-family:'Playfair Display',serif;font-weight:700;white-space:nowrap;transform:translate(-50%,-50%)}
.brand__dot{width:.5em;height:.5em;border-radius:50%;background:currentColor;flex:none}
.brand--gold{color:var(--gold)}
.brand--white{color:#fff}
.shadow{box-shadow:0 6px 8px rgba(0,0,0,.18)}
/* letterhead */
.letterhead{position:absolute;left:112px;top:383px;width:476px;height:671px;background:var(--paper);overflow:hidden}
.letterhead__reg{position:absolute;left:25px;top:106px;font-size:7px;color:var(--muted)}
.contact{position:absolute;font-size:6.2px;line-height:8.2px;color:var(--muted)}
.contact li{list-style:none;display:flex;gap:4px;align-items:flex-start}
.contact svg{width:6px;height:6px;flex:none;margin-top:1px}
.letterhead__contact{left:355px;top:44px}
.letterhead__watermark{position:absolute;left:238px;top:345px;transform:translate(-50%,-50%);font-family:'Playfair Display',serif;font-weight:700;font-size:46px;color:var(--blue);opacity:.05;white-space:nowrap}
.letter{position:absolute;left:23px;top:170px;width:430px;font-size:7px;color:var(--muted);line-height:12.7px}
.letter__date{margin-bottom:7px}
.letter__recipient{line-height:8.6px;margin-bottom:40px}
.letter__greeting{margin-bottom:20px}
.letter p{margin-bottom:10px}
.signature{position:absolute;left:24px;top:423px;width:110px;height:32px;background:linear-gradient(90deg,rgba(40,50,140,.12),rgba(40,50,140,.04))}
.signer{position:absolute;left:23px;top:457px}
.signer__name{font-size:12px;color:var(--ink)}
.signer__role{font-size:6.5px;color:var(--muted)}
.letterhead__footer{position:absolute;left:0;bottom:0;width:476px;height:56px}
.letterhead__footnote{position:absolute;left:0;right:0;bottom:15px;text-align:center;font-size:6.5px;color:#fff}
/* business cards */
.card{position:absolute;left:577px;width:223px;height:128px;overflow:hidden}
.card--front{top:506px;background:var(--paper)}
.card--back{top:647px;background:var(--blue)}
.card__contact{left:21px;top:73px;font-size:4.6px;line-height:7.2px}
.card__contact svg{width:4.5px;height:4.5px}
.card__name{position:absolute;left:138px;top:76px;font-family:'Playfair Display',serif;font-weight:700;font-size:7.5px;color:var(--gold)}
.card__role{position:absolute;left:138px;top:86px;font-size:4.5px;color:var(--blue)}
.card__band{position:absolute;left:0;bottom:0;width:223px;height:30px}
.card__address{position:absolute;left:0;right:0;bottom:7px;text-align:center;font-size:4.5px;color:#fff}
/* email signature */
.email{position:absolute;left:604px;top:827px;width:514px;height:118px;background:var(--paper);overflow:hidden}
.email__side{position:absolute;left:0;top:0;width:110px;height:118px}
.email__photo{position:absolute;left:26px;top:20px;width:78px;height:78px;border-radius:50%;border:3px solid #fff;background:radial-gradient(circle at 50% 40%,#c9c2bb,#8a857f 60%,#3b3f47)}
.email__name{position:absolute;left:133px;top:6px;font-family:'Playfair Display',serif;font-weight:700;font-size:25px;color:var(--gold-light)}
.email__role{position:absolute;left:134px;top:40px;font-size:11.5px;letter-spacing:2.6px;color:var(--blue)}
.email__contact{font-size:8.8px;line-height:15.5px;color:var(--ink)}
.email__contact svg{width:7px;height:7px;margin-top:3px}
.email__contact--left{left:133px;top:66px}
.email__contact--right{left:211px;top:66px;line-height:10.5px}
.email__contact--right li:first-child{margin-bottom:5px}
.social{position:absolute;left:400px;top:94px;display:flex;gap:12px}
.social span{width:9px;height:9px;border-radius:50%;background:#2b3a4a}
</style>
</head>
<body>
<main class="canvas">
  <section class="panel panel--light">
    <div class="brand brand--gold" style="left:432px;top:127px;font-size:30px"><span class="brand__dot" style="background:var(--blue)"></span>TK Morenkwe Inc.</div>
  </section>
  <section class="panel panel--dark">
    <div class="brand brand--white" style="left:153px;top:127px;font-size:30px"><span class="brand__dot"></span>TK Morenkwe Inc.</div>
  </section>
  <section class="panel panel--board"></section>

  <article class="letterhead shadow">
    <div class="brand brand--gold" style="left:60px;top:73px;font-size:10px">TK Morenkwe Inc.</div>
    <p class="letterhead__reg">Reg: 2020/000000/01</p>
    <ul class="contact letterhead__contact">
      <li><svg viewBox="0 0 10 10"><path d="M2 1l2 2-1 1.5a6 6 0 0 0 2.5 2.5L7 6l2 2-1.5 1.5C4.5 9 1 5.5.5 2.5z" fill="var(--gold)"/></svg>011 000 0100</li>
      <li><svg viewBox="0 0 10 10"><rect x="1" y="4" width="8" height="5" fill="var(--gold)"/><rect x="2.5" y="1" width="5" height="3" fill="none" stroke="var(--gold)"/></svg>086 000 0200</li>
      <li><svg viewBox="0 0 10 10"><path d="M0 5L10 0 7 10 5 6z" fill="var(--gold)"/></svg>info@tkmorenkwe.co.za</li>
      <li style="margin-top:2px"><svg viewBox="0 0 10 10"><path d="M4 6l2-2M3 5L1.5 6.5a1.8 1.8 0 0 0 2 2L5 7M7 5l1.5-1.5a1.8 1.8 0 0 0-2-2L5 3" stroke="var(--gold)" fill="none" stroke-width="1.2"/></svg>www.tkmorenkwe.co.za</li>
      <li style="margin-top:2px"><svg viewBox="0 0 10 10"><path d="M5 10S1.5 6 1.5 4a3.5 3.5 0 0 1 7 0c0 2-3.5 6-3.5 6z" fill="var(--gold)"/><circle cx="5" cy="4" r="1.3" fill="#fff"/></svg>Block B Riverside Office Park<br>12 Oak road north<br>Sandton 2000</li>
    </ul>
    <div class="letterhead__watermark">TK Morenkwe</div>
    <div class="letter">
      <p class="letter__date">11.10.2019</p>
      <p class="letter__recipient">Recipient name<br>45 Maple Ave.<br>Riverton, PA 10000</p>
      <p class="letter__greeting">Dear, Mr___________</p>
      <p>Lorem Ipsum is simply dummy text of the printing and typesetting industry. Lorem Ipsum has been the industry's standard dummy text ever since the1500s,when an unknown printer took a galley of type and scrambled it to make a type specimen book. It has survived not only five centuries, but also the leap into electronic typesetting, remaining essentially unchanged.</p>
      <p style="margin-top:13px">Lorem Ipsum is simply dummy text of the printing and typesetting industry. Lorem Ipsum has been the industry's standard dummy text ever since the1500s.</p>
      <p style="margin-top:13px">Lorem Ipsum is simply dummy text of the printing and typesetting industry.</p>
    </div>
    <div class="signature" role="img" aria-label="Handwritten signature"></div>
    <div class="signer">
      <p class="signer__name">Thabo Kgosi</p>
      <p class="signer__role">Director</p>
    </div>
    <svg class="letterhead__footer" viewBox="0 0 476 56" preserveAspectRatio="none">
      <path d="M0 34Q238 -18 476 34V56H0z" fill="var(--gold)"/>
      <path d="M0 42Q238 -6 476 42V56H0z" fill="var(--blue)"/>
    </svg>
    <p class="letterhead__footnote">Director: Thabo Kgosi Morenkwe BA, LLB and HDip Tax Law</p>
  </article>

  <article class="card card--front shadow">
    <div class="brand brand--gold" style="left:111px;top:40px;font-size:8px">TK Morenkwe Inc.</div>
    <ul class="contact card__contact">
      <li><svg viewBox="0 0 10 10"><path d="M2 1l2 2-1 1.5a6 6 0 0 0 2.5 2.5L7 6l2 2-1.5 1.5C4.5 9 1 5.5.5 2.5z" fill="var(--gold)"/></svg>011 000 0100</li>
      <li><svg viewBox="0 0 10 10"><rect x="1" y="4" width="8" height="5" fill="var(--gold)"/><rect x="2.5" y="1" width="5" height="3" fill="none" stroke="var(--gold)"/></svg>086 000 0200</li>
      <li><svg viewBox="0 0 10 10"><path d="M0 5L10 0 7 10 5 6z" fill="var(--gold)"/></svg>tumi@tkmorenkwe.co.za</li>
    </ul>
    <p class="card__name">Tumi Morenkwe</p>
    <p class="card__role">Director</p>
    <svg class="card__band" viewBox="0 0 223 30" preserveAspectRatio="none">
      <path d="M0 18Q111 -2 223 18V30H0z" fill="var(--gold)"/>
      <path d="M0 22Q111 3 223 22V30H0z" fill="var(--blue)"/>
      <path d="M112 15S107 9 107 6.5a5 5 0 0 1 10 0C117 9 112 15 112 15z" fill="#fff" stroke="var(--gold)" stroke-width="1.2"/>
      <circle cx="112" cy="6.5" r="2" fill="none" stroke="var(--gold)"/>
    </svg>
    <p class="card__address">Block B Riverside Office Park 12 Oak road north Sandton 2000</p>
  </article>

  <article class="card card--back shadow">
    <div class="brand brand--white" style="left:111px;top:64px;font-size:10px">TK Morenkwe Inc.</div>
  </article>

  <article class="email shadow">
    <svg class="email__side" viewBox="0 0 110 118" preserveAspectRatio="none">
      <path d="M0 0H78Q118 59 78 118H0z" fill="var(--gold)"/>
      <path d="M0 0H73Q111 59 73 118H0z" fill="var(--blue)"/>
    </svg>
    <div class="email__photo" role="img" aria-label="Portrait photograph of the director"></div>
    <p class="email__name">Tumi Morenkwe</p>
    <p class="email__role">Director</p>
    <ul class="contact email__contact email__contact--left">
      <li><svg viewBox="0 0 10 10"><path d="M2 1l2 2-1 1.5a6 6 0 0 0 2.5 2.5L7 6l2 2-1.5 1.5C4.5 9 1 5.5.5 2.5z" fill="var(--gold-light)"/></svg>011 000 0100</li>
      <li><svg viewBox="0 0 10 10"><rect x="1" y="4" width="8" height="5" fill="var(--gold-light)"/><rect x="2.5" y="1" width="5" height="3" fill="none" stroke="var(--gold-light)"/></svg>086 000 0200</li>
    </ul>
    <ul class="contact email__contact email__contact--right">
      <li><svg viewBox="0 0 10 10"><path d="M0 5L10 0 7 10 5 6z" fill="var(--gold-light)"/></svg>tumi@tkmorenkwe.co.za</li>
      <li><svg viewBox="0 0 10 10"><path d="M5 10S1.5 6 1.5 4a3.5 3.5 0 0 1 7 0c0 2-3.5 6-3.5 6z" fill="none" stroke="var(--gold-light)"/></svg>Block B Riverside Office Park12<br>Oak road north Sandton 2000</li>
    </ul>
    <div class="brand brand--gold" style="left:440px;top:44px;font-size:10px">TK Morenkwe Inc.</div>
    <div class="social"><span></span><span></span><span></span><span></span><span></span></div>
  </article>
</main>
</body>
</html>
```